Clean, minimal label design needed for new skincare line.

Want clean, minimal labels for Clean (non-toxic), cosmeceutical grade Australian-made skincare products. We are going for a minimal and simple approach to our branding so want the labelling to follow suit. Please find logos attached below. Labels are white and logo is black. Font to be black, avoid colours other than white or black.

Target Market(s)

25-65+

Industry/Entity Type

Beauty

Requirements
Must have
• On the front:
- logo
- product name eg. moisturiser 1
- descriptive words eg. light
- weight eg. 30mls/1 fl oz

On the back:
- directions eg. apply one pump both AM and PM after serum application and prior to barrier protect application.
- Cruelty free icon
- Vegan icon
- Made in Australia Icon
- Open jar with 12M Icon
Nice to have
• See above
Should not have
• Avoid colours other than white or black.

```html
<!DOCTYPE html>
<html lang="en">
<head>
<meta charset="utf-8">
<title>Stillwater Co. Skincare – Moisturiser 1 Label</title>
<link href="https://fonts.googleapis.com/css2?family=Oswald:wght@400;500;600&display=swap" rel="stylesheet">
<style>
  :root {
    --ink: #111111;
    --paper: #ffffff;
    --backdrop: #ececec;
    --rule: #1a1a1a;
  }
  * { box-sizing: border-box; margin: 0; padding: 0; }
  html, body {
    width: 1200px;
    height: 800px;
    overflow: hidden;
    background: var(--backdrop);
  }
  .canvas {
    width: 1200px;
    height: 800px;
    display: flex;
    align-items: center;
    justify-content: center;
  }
  .label {
    width: 420px;
    height: 740px;
    background: var(--paper);
    padding: 40px 36px;
    display: flex;
    flex-direction: column;
    color: var(--ink);
    font-family: "Oswald", "Arial Narrow", sans-serif;
    box-shadow: 0 2px 10px rgba(0,0,0,0.08);
  }
  .brand-block {
    width: 320px;
    height: 320px;
    background: var(--ink);
    margin-left: 14px;
  }
  .brand {
    margin-top: 26px;
    margin-left: 14px;
  }
  .brand-name {
    font-size: 40px;
    font-weight: 600;
    line-height: 1;
    letter-spacing: -0.5px;
  }
  .brand-line {
    font-size: 17px;
    font-weight: 400;
    letter-spacing: 1px;
    margin-top: 2px;
    padding-left: 112px;
  }
  .product-table {
    margin-top: 24px;
    border: 1.5px solid var(--rule);
    display: flex;
    flex-direction: column;
  }
  .product-name {
    font-size: 29px;
    font-weight: 600;
    letter-spacing: 0.5px;
    text-align: center;
    padding: 14px 0 12px;
    border-bottom: 1.5px solid var(--rule);
  }
  .product-texture {
    font-size: 19px;
    font-weight: 600;
    letter-spacing: 0.5px;
    text-align: center;
    padding: 10px 0;
    border-bottom: 1.5px solid var(--rule);
  }
  .product-meta {
    display: flex;
    align-items: center;
    padding: 14px 16px;
  }
  .skin-type {
    font-size: 19px;
    font-weight: 600;
    letter-spacing: 0.5px;
    line-height: 1.05;
    flex: 1;
  }
  .divider {
    width: 1.5px;
    height: 42px;
    background: var(--rule);
    margin: 0 16px;
  }
  .volume {
    font-size: 18px;
    font-weight: 500;
    letter-spacing: 0.5px;
    flex: 1.2;
    text-align: center;
  }
</style>
</head>
<body>
  <main class="canvas">
    <section class="label">
      <div class="brand-block"></div>
      <div class="brand">
        <div class="brand-name">stillwater co.</div>
        <div class="brand-line">skincare</div>
      </div>
      <div class="product-table">
        <div class="product-name">Moisturiser 1</div>
        <div class="product-texture">LIGHT</div>
        <div class="product-meta">
          <div class="skin-type">FOR ALL<br>SKIN TYPES</div>
          <div class="divider"></div>
          <div class="volume">30mls/1 fl oz</div>
        </div>
      </div>
    </section>
  </main>
</body>
</html>
```